NEED A BUSINESS CARD FOR A NEW ELECTRICAL BUSINESS

HI I am after a new business card for my new electrical business I have a logo that I have attached its the one in blue, I would like that on the front and on the back my name- Leonard Pike, Email leonardpike@tallmesh.com, mobile 0491362047, licence no# vic 47819, nsw 591304k I wont something that is a stand out from the rest but at the same time is neat as being a new business I wont it to catch peoples eye on the front of the card I would like the logo and not much else.
And on the back as well I would like a slogan saying something like
Quality-Reliable-Service

Hi all on the back of the card I would like a little slogan like Quality-Reliable-Service something like that would be good thanks

Hi all the business card needs to have both these licence numbers on it                                                  VIC-47819 nsw-591304k

```html
<!DOCTYPE html>
<html lang="en">
<head>
<meta charset="utf-8">
<title>Leonard Pike Electrical – Business Cards</title>
<link rel="stylesheet" href="https://fonts.googleapis.com/css2?family=Roboto:wght@300;400;500;700&display=swap">
<style>
  :root {
    --backdrop: #e6e4e1;
    --card-dark: #1b1c1e;
    --card-mid: #2b2c2f;
    --accent-blue: #1e86d6;
    --name-grey: #8d8f93;
    --text-light: #eceef0;
    --divider: #4a4c50;
    --slogan-grey: #6f7175;
  }
  html, body {
    margin: 0;
    padding: 0;
    width: 1200px;
    height: 838px;
    overflow: hidden;
    background: var(--backdrop);
  }
  .canvas {
    width: 1200px;
    height: 838px;
    display: flex;
    flex-direction: column;
    align-items: center;
    justify-content: center;
    gap: 32px;
  }
  .business-card {
    position: relative;
    width: 640px;
    height: 366px;
    background: radial-gradient(ellipse at 55% 40%, var(--card-mid) 0%, var(--card-dark) 75%);
    box-shadow: 0 14px 32px rgba(0,0,0,0.25);
    font-family: "Roboto", Arial, sans-serif;
    color: var(--text-light);
    overflow: hidden;
  }
  .brand {
    position: absolute;
    left: 0;
    right: 0;
    display: flex;
    flex-direction: column;
    align-items: center;
  }
  .card-front .brand { top: 140px; }
  .card-back .brand { top: 70px; }
  .brand-name {
    display: flex;
    align-items: center;
    gap: 14px;
    font-size: 28px;
    font-weight: 700;
    letter-spacing: 3px;
    color: var(--accent-blue);
    text-transform: uppercase;
    white-space: nowrap;
  }
  .brand-square {
    width: 22px;
    height: 22px;
    background: var(--accent-blue);
  }
  .licence-line {
    margin-top: 12px;
    font-size: 14px;
    font-weight: 500;
    color: var(--accent-blue);
    letter-spacing: 0.4px;
  }
  .holder-name {
    position: absolute;
    left: 48px;
    top: 212px;
    font-size: 22px;
    letter-spacing: 1px;
    text-transform: uppercase;
    white-space: nowrap;
  }
  .holder-name .first { font-weight: 700; color: var(--accent-blue); }
  .holder-name .last { font-weight: 300; color: var(--name-grey); }
  .contact-divider {
    position: absolute;
    left: 282px;
    top: 196px;
    width: 1px;
    height: 66px;
    background: var(--divider);
  }
  .contact-list {
    position: absolute;
    left: 304px;
    top: 198px;
    margin: 0;
    padding: 0;
    list-style: none;
  }
  .contact-item {
    display: flex;
    align-items: center;
    gap: 16px;
    height: 30px;
    font-size: 17px;
    white-space: nowrap;
  }
  .contact-item.phone { font-weight: 700; letter-spacing: 1px; }
  .contact-item.email { font-weight: 400; }
  .contact-icon { width: 13px; height: 13px; flex: none; }
  .contact-icon.phone-icon { fill: var(--accent-blue); }
  .contact-icon.mail-icon { fill: none; stroke: var(--accent-blue); stroke-width: 2.4; }
  .slogan {
    position: absolute;
    left: 0;
    right: 0;
    bottom: 26px;
    text-align: center;
    font-size: 13px;
    font-weight: 500;
    letter-spacing: 3px;
    text-transform: uppercase;
    color: var(--slogan-grey);
  }
</style>
</head>
<body>
<main class="canvas">
  <section class="business-card card-front">
    <div class="brand">
      <div class="brand-name"><span class="brand-square"></span>Leonard Pike Electrical</div>
      <div class="licence-line">licence no# vic 47819, nsw 591304k</div>
    </div>
  </section>

  <section class="business-card card-back">
    <div class="brand">
      <div class="brand-name"><span class="brand-square"></span>Leonard Pike Electrical</div>
      <div class="licence-line">licence no# vic 47819, nsw 591304k</div>
    </div>

    <div class="holder-name"><span class="first">Leonard</span> <span class="last">Pike</span></div>

    <div class="contact-divider"></div>

    <ul class="contact-list">
      <li class="contact-item phone">
        <svg class="contact-icon phone-icon" viewBox="0 0 24 24" aria-hidden="true"><path d="M6.6 10.8c1.4 2.8 3.8 5.1 6.6 6.6l2.2-2.2c.3-.3.7-.4 1-.2 1.1.4 2.3.6 3.6.6.6 0 1 .4 1 1V20c0 .6-.4 1-1 1C10.6 21 3 13.4 3 4c0-.6.4-1 1-1h3.5c.6 0 1 .4 1 1 0 1.3.2 2.5.6 3.6.1.3 0 .7-.2 1z"/></svg>
        <span>049 136 2047</span>
      </li>
      <li class="contact-item email">
        <svg class="contact-icon mail-icon" viewBox="0 0 24 24" aria-hidden="true"><rect x="2.5" y="5.5" width="19" height="13"/><path d="M2.5 5.5l9.5 7.5 9.5-7.5"/></svg>
        <span>leonardpike@tallmesh.com</span>
      </li>
    </ul>

    <div class="slogan">Quality – Reliable – Service</div>
  </section>
</main>
</body>
</html>
```